bluefernworks.com website design

We're looking for a website design for Bluefernworks.com .
Bluefern is a manufacturer of high visibility traffic safety equipment and gear.. Our initial site will be a product catalog site featuring traffic cones . We will eventually expand to include traffic barriers, mesh signs, safety clothing and more. Our logo and product pictures can be found at bluefernworks.com .
Updates

Target Market(s)

We service a wide range of customers with our focus markets being construction, manufacturing and municipalities.

Industry/Entity Type

Safety Products

Number of Pages Required

1 page

Font styles to use
Sans Serif

Requirements
Must have
• company logo w/compatible color scheme

```html
<!DOCTYPE html>
<html lang="en">
<head>
<meta charset="utf-8">
<title>Bluefern Safety Products</title>
<link href="https://fonts.googleapis.com/css2?family=Montserrat:wght@400;500;600;700;800&display=swap" rel="stylesheet">
<style>
:root{
  --orange:#e8913a;
  --orange-text:#e8782a;
  --hero-a:#f0900e;
  --hero-b:#f6b817;
  --beige:#f2efe4;
  --grey-bg:#f3f3f3;
  --yellow:#f2d648;
  --olive:#7a6a2a;
  --ink:#1d1d1d;
  --body:#333;
  --field:#f2f2f2;
  --line:#d6d6d6;
  --footer:#444444;
  --white:#ffffff;
}
*{box-sizing:border-box;margin:0;padding:0}
html,body{width:1200px;height:3400px;overflow:hidden}
body{font-family:'Montserrat',sans-serif;color:var(--ink);background:var(--white);position:relative}

/* header */
.site-header{position:absolute;left:0;top:0;width:1200px;height:106px;background:var(--white)}
.brand{position:absolute;left:113px;top:34px;display:flex;align-items:center;gap:10px;font-size:26px;font-weight:700;color:var(--orange)}
.brand-dot{width:26px;height:26px;border-radius:50%;background:var(--orange)}
.nav{position:absolute;top:44px;font-size:14px;font-weight:500;color:var(--ink)}
.nav svg{vertical-align:middle;margin-left:8px}
.btn{position:absolute;display:flex;align-items:center;justify-content:center;border-radius:30px;font-weight:600;font-size:17px}
.btn-orange{background:var(--orange);color:var(--white)}
.btn-white{background:var(--white);color:var(--orange-text)}

/* hero */
.hero{position:absolute;left:0;top:106px;width:1200px;height:569px;background:linear-gradient(100deg,var(--hero-a),var(--hero-b) 45%,var(--hero-a));overflow:hidden}
.hero-skyline{position:absolute;left:0;top:300px;width:1200px;height:269px;background:linear-gradient(180deg,rgba(226,118,22,0) 0%,rgba(226,118,22,.55) 40%,rgba(214,100,14,.85) 100%)}
.hero-figure{position:absolute;left:760px;top:80px;width:400px;height:489px;border-radius:200px 200px 0 0;background:radial-gradient(ellipse at 50% 35%,#f7c25a 0%,#ee8a2c 55%,rgba(230,120,30,.6) 100%)}
.hero-title{position:absolute;left:110px;top:100px;width:440px;font-size:36px;font-weight:600;line-height:41px;color:var(--white)}
.hero-text{position:absolute;left:110px;top:244px;width:400px;font-size:13.5px;line-height:21px;color:var(--white)}

/* intro */
.intro{position:absolute;left:0;top:675px;width:1200px;height:467px;background:var(--beige)}
.intro-title{position:absolute;left:108px;top:772px;font-size:27px;font-weight:600}
.intro-text{position:absolute;left:108px;top:836px;width:508px;font-size:13.2px;line-height:20px;color:var(--body)}

.quote-form{position:absolute;left:655px;top:591px;width:433px;height:497px;background:var(--white);border-radius:20px;box-shadow:0 4px 18px rgba(0,0,0,.06)}
.label{position:absolute;font-size:13.5px;color:var(--body)}
.label b{color:#e03a2a;font-weight:500}
.field{position:absolute;background:var(--field);font-size:13.5px;color:#a3a3a3;padding:0 16px;display:flex;align-items:center}
.field.plain{background:transparent}
.field.area{align-items:flex-start;padding-top:12px}

/* products */
.products{position:absolute;left:0;top:1142px;width:1200px;height:1205px;background:var(--grey-bg)}
.banner{position:absolute;left:156px;top:1222px;width:888px;height:241px;background:var(--yellow);border-radius:20px;overflow:hidden}
.banner-band{position:absolute;left:0;bottom:0;width:516px;height:56px;background:var(--olive)}
.banner-art{position:absolute;left:548px;top:0;width:340px;height:241px;background:radial-gradient(ellipse at 55% 60%,#f07a3a 0%,#f29a48 40%,#f3c252 70%,var(--yellow) 100%)}
.banner-kicker{position:absolute;left:224px;top:1280px;font-size:28px;font-weight:600}
.banner-title{position:absolute;left:224px;top:1320px;font-size:42px;font-weight:800;letter-spacing:1px}

.card{position:absolute;width:268px;height:356px;background:var(--white);border:1px solid #cfcfcf}
.tag{position:absolute;left:3px;top:15px;width:108px;height:48px;background:var(--yellow);clip-path:polygon(0 0,86% 0,100% 100%,0 100%);font-size:11px;line-height:13px;padding:10px 0 0 18px;color:var(--ink);z-index:1}
.photo{position:absolute;left:84px;top:22px;width:100px;height:170px;border-radius:8px}
.photo.orange{background:linear-gradient(180deg,#fbe2cf,#f5a56c)}
.photo.red{background:linear-gradient(180deg,#fbd6cc,#f0705a)}
.photo.lime{background:linear-gradient(180deg,#e6f8cf,#a6e85c)}
.code{position:absolute;left:0;top:208px;width:100%;text-align:center;font-size:16.5px;font-weight:500;color:var(--orange-text)}
.desc{position:absolute;left:0;top:230px;width:100%;text-align:center;font-size:12.5px;line-height:17px;color:var(--ink)}
.specs{position:absolute;left:0;top:280px;width:100%;border-top:1px solid var(--line);display:grid;grid-template-columns:repeat(4,1fr);padding:14px 24px 0;text-align:center;font-size:11.5px;row-gap:10px}
.specs .k{color:var(--orange-text)}
.specs .v{color:var(--ink)}

/* cta */
.cta{position:absolute;left:110px;top:2297px;width:980px;height:171px;border-radius:12px;background:linear-gradient(90deg,#7a4a2a,#b0612e 35%,#8a5030 70%,#5e3a22)}
.cta-title{position:absolute;left:183px;top:2360px;font-size:26px;font-weight:600;color:var(--white)}

/* why */
.why-title{position:absolute;left:0;top:2542px;width:1200px;text-align:center;font-size:27px;font-weight:600}
.why-item{position:absolute;width:240px;text-align:center}
.why-icon{width:84px;height:84px;margin:0 auto;border:2px solid var(--orange);border-radius:50%;display:flex;align-items:center;justify-content:center}
.why-head{margin-top:40px;font-size:17.5px;font-weight:600}
.why-text{width:190px;margin:20px auto 0;font-size:13.5px;line-height:17px;color:var(--ink)}
.divider{position:absolute;top:2627px;width:1px;height:237px;background:var(--line)}

.street-scene{position:absolute;left:0;top:2904px;width:1200px;height:240px;background:linear-gradient(180deg,#ffffff 0,#f8dcc4 45%,#cfe6c4 72%,#8e98a3 86%,#7c8690)}

/* footer */
.site-footer{position:absolute;left:0;top:3144px;width:1200px;height:256px;background:var(--footer);color:var(--white)}
.f-brand{position:absolute;left:139px;top:88px;display:flex;align-items:center;gap:10px;font-size:27px;font-weight:700;color:var(--orange)}
.f-copy{position:absolute;left:152px;top:164px;font-size:13px;color:#c9c9c9}
.f-head{position:absolute;font-size:17px;font-weight:500}
.f-line{position:absolute;font-size:13.5px;display:flex;align-items:center;gap:14px}
.f-link{position:absolute;left:719px;font-size:13.5px}
.social{position:absolute;top:70px;width:20px;height:20px;border-radius:50%;background:var(--white)}
</style>
</head>
<body>

<header class="site-header">
  <div class="brand"><span class="brand-dot"></span>Bluefern</div>
  <span class="nav" style="left:519px">Home</span>
  <span class="nav" style="left:582px">About Us</span>
  <span class="nav" style="left:676px">Products<svg width="14" height="9" viewBox="0 0 14 9"><path d="M1 1l6 6 6-6" fill="none" stroke="#1d1d1d" stroke-width="1.6"/></svg></span>
  <span class="nav" style="left:789px">Contact Us</span>
  <a class="btn btn-orange" style="left:920px;top:30px;width:170px;height:43px">Get a quote</a>
</header>

<section class="hero">
  <div class="hero-skyline" role="img" aria-label="Illustrated city skyline with a crane and traffic cones"></div>
  <div class="hero-figure" role="img" aria-label="Illustration of a waving construction worker in a hard hat and hi-vis vest"></div>
  <h1 class="hero-title">Manufacturer of Traffic Control and Personal Safety Products</h1>
  <p class="hero-text">One of the leading manufacturers and suppliers of safety equipment. As a professional PPE supplier, we can supply Traffic Equipment, safety shoes, work boots, coveralls, FR coveralls, helmets, glasses, safety gloves and more.</p>
  <a class="btn btn-white" style="left:113px;top:348px;width:171px;height:44px">Contact Us</a>
</section>

<section class="intro"></section>
<h2 class="intro-title">Reliable Safety Equipment Supplier</h2>
<p class="intro-text">Lorem ipsum dolor sit amet consectetur. Tellus vitae morbi ipsum rutrum. Nulla potenti mollis nulla volutpat convallis. Cras vestibulum platea amet nulla faucibus ornare dolor sit. Commodo nec donec nullam vestibulum euismod nisl egestas condimentum. Fermentum molestie pulvinar in in massa ultrices. Dictumst eget quam lectus massa arcu posuere bibendum elementum. Lorem consectetur fermentum nec magna ut quis scelerisque. Scelerisque egestas massa viverra purus at nullam. Diam porttitor egestas auctor augue. Nec nunc eu dui etiam. Pulvinar nunc nam donec mi sit arcu a orci potenti. Odio placerat mattis nam elementum sed.</p>

<form class="quote-form">
  <span class="label" style="left:41px;top:46px">First name<b>*</b></span>
  <span class="label" style="left:224px;top:46px">Last name<b>*</b></span>
  <span class="field plain" style="left:44px;top:78px;width:160px;height:30px">First name</span>
  <span class="field plain" style="left:218px;top:78px;width:180px;height:30px">Last name</span>
  <span class="label" style="left:41px;top:129px">Email<b>*</b></span>
  <span class="field" style="left:38px;top:157px;width:356px;height:39px">Email</span>
  <span class="label" style="left:38px;top:209px">Company<b>*</b></span>
  <span class="field" style="left:38px;top:237px;width:356px;height:38px">Company name</span>
  <span class="label" style="left:41px;top:292px">Message</span>
  <span class="field area" style="left:38px;top:315px;width:356px;height:75px">Your message</span>
  <a class="btn btn-orange" style="left:37px;top:416px;width:169px;height:42px">Send</a>
</form>

<section class="products"></section>
<div class="banner">
  <div class="banner-band"></div>
  <div class="banner-art" role="img" aria-label="Traffic cones with a yellow hard hat"></div>
</div>
<p class="banner-kicker">Our Products</p>
<h2 class="banner-title">TRAFFIC CONE</h2>

<article class="card" style="left:154px;top:1509px">
  <div class="tag">2 Reflective<br>Collars</div>
  <div class="photo orange" role="img" aria-label="Photo of a 28 inch orange traffic cone with two reflective collars"></div>
  <p class="code">2810064B</p>
  <p class="desc">28" 10lb Orange Cone w/(2)<br>HV Reflective Collars</p>
  <div class="specs"><span class="k">Height</span><span class="k">Base</span><span class="k">Weight</span><span class="k">Color</span><span class="v">28"</span><span class="v">15'"</span><span class="v">10 lb</span><span class="v">Orange</span></div>
</article>
<article class="card" style="left:453px;top:1509px">
  <div class="tag">2 Reflective<br>Collars</div>
  <div class="photo orange" role="img" aria-label="Photo of a 36 inch orange traffic cone with two reflective collars"></div>
  <p class="code">3612064B</p>
  <p class="desc">36" 12lb Orange Cone w/(2)<br>HV Reflective Collars</p>
  <div class="specs"><span class="k">Height</span><span class="k">Base</span><span class="k">Weight</span><span class="k">Color</span><span class="v">28"</span><span class="v">15'"</span><span class="v">10 lb</span><span class="v">Orange</span></div>
</article>
<article class="card" style="left:752px;top:1509px">
  <div class="tag">No Reflective<br>Collars</div>
  <div class="photo red" role="img" aria-label="Photo of a plain red-orange traffic cone"></div>
  <p class="code">2810064B</p>
  <p class="desc">28" 10lb Orange Cone w/(2)<br>HV Reflective Collars</p>
  <div class="specs"><span class="k">Height</span><span class="k">Base</span><span class="k">Weight</span><span class="k">Color</span><span class="v">28"</span><span class="v">15'"</span><span class="v">10 lb</span><span class="v">Orange</span></div>
</article>

<article class="card" style="left:157px;top:1893px">
  <div class="tag">2 Reflective<br>Collars</div>
  <div class="photo lime" role="img" aria-label="Photo of a lime green traffic cone with two reflective collars"></div>
  <p class="code">2810064B</p>
  <p class="desc">28" 10lb Orange Cone w/(2)<br>HV Reflective Collars</p>
  <div class="specs"><span class="k">Height</span><span class="k">Base</span><span class="k">Weight</span><span class="k">Color</span><span class="v">28"</span><span class="v">15'"</span><span class="v">10 lb</span><span class="v">Orange</span></div>
</article>
<article class="card" style="left:456px;top:1893px">
  <div class="tag">2 Reflective<br>Collars</div>
  <div class="photo orange" role="img" aria-label="Photo of an orange traffic cone with two reflective collars"></div>
  <p class="code">2810064B</p>
  <p class="desc">28" 10lb Orange Cone w/(2)<br>HV Reflective Collars</p>
  <div class="specs"><span class="k">Height</span><span class="k">Base</span><span class="k">Weight</span><span class="k">Color</span><span class="v">28"</span><span class="v">15'"</span><span class="v">10 lb</span><span class="v">Orange</span></div>
</article>
<article class="card" style="left:755px;top:1893px">
  <div class="tag">2 Reflective<br>Collars</div>
  <div class="photo lime" role="img" aria-label="Photo of a plain green traffic cone"></div>
  <p class="code">2810064B</p>
  <p class="desc">28" 10lb Orange Cone w/(2)<br>HV Reflective Collars</p>
  <div class="specs"><span class="k">Height</span><span class="k">Base</span><span class="k">Weight</span><span class="k">Color</span><span class="v">28"</span><span class="v">15'"</span><span class="v">10 lb</span><span class="v">Orange</span></div>
</article>

<div class="cta" role="img" aria-label="Photo of a row of traffic cones on a road"></div>
<h2 class="cta-title">Start Doing Business with Us Today!</h2>
<a class="btn btn-white" style="left:792px;top:2357px;width:169px;height:43px">Get a quote</a>

<h2 class="why-title">Why Choose Us</h2>
<div class="divider" style="left:366px"></div>
<div class="divider" style="left:609px"></div>
<div class="divider" style="left:851px"></div>

<div class="why-item" style="left:122px;top:2628px">
  <div class="why-icon"><svg width="40" height="40" viewBox="0 0 40 40" fill="none" stroke="#e8913a" stroke-width="2.4"><circle cx="20" cy="16" r="11"/><path d="M15 16l4 4 7-8"/><path d="M13 25l-3 12 10-5 10 5-3-12"/></svg></div>
  <h3 class="why-head">Good Quality Control</h3>
  <p class="why-text">Lorem ipsum dolor sit amet consectetur. Ipsum mattis non purus viverra netus. Adipiscing eu</p>
</div>
<div class="why-item" style="left:368px;top:2626px">
  <div class="why-icon"><svg width="40" height="40" viewBox="0 0 40 40" fill="none" stroke="#e8913a" stroke-width="2.4"><path d="M14 8h12l-3 6c7 3 10 10 9 16-1 4-4 6-12 6s-11-2-12-6c-1-6 2-13 9-16z"/><text x="20" y="31" font-size="14" font-family="Montserrat,sans-serif" font-weight="700" fill="#e8913a" stroke="none" text-anchor="middle">$</text></svg></div>
  <h3 class="why-head">Direct Factory Price</h3>
  <p class="why-text">Lorem ipsum dolor sit amet consectetur. Ipsum mattis non purus viverra netus. Adipiscing eu</p>
</div>
<div class="why-item" style="left:615px;top:2628px">
  <div class="why-icon"><svg width="44" height="40" viewBox="0 0 44 40" fill="none" stroke="#e8913a" stroke-width="2.4"><rect x="8" y="10" width="20" height="16"/><path d="M28 15h7l5 6v5H28z"/><circle cx="15" cy="29" r="3.5"/><circle cx="34" cy="29" r="3.5"/><path d="M2 14h5M0 19h7M3 24h4"/></svg></div>
  <h3 class="why-head">Fast Delivery Time</h3>
  <p class="why-text">Lorem ipsum dolor sit amet consectetur. Ipsum mattis non purus viverra netus. Adipiscing eu</p>
</div>
<div class="why-item" style="left:858px;top:2624px">
  <div class="why-icon"><svg width="40" height="40" viewBox="0 0 40 40" fill="none" stroke="#e8913a" stroke-width="2.4"><path d="M20 4l2.5 5 5.5.8-4 3.9 1 5.5-5-2.6-5 2.6 1-5.5-4-3.9 5.5-.8z"/><path d="M7 24h6v12H7zM13 26h8l5-6c2 0 3 1 3 3l-2 5h7c2 0 3 2 2 4l-2 4H13"/></svg></div>
  <h3 class="why-head">Customer Satisfaction</h3>
  <p class="why-text">Lorem ipsum dolor sit amet consectetur. Ipsum mattis non purus viverra netus. Adipiscing eu</p>
</div>

<div class="street-scene" role="img" aria-label="Illustrated street with workers, traffic cones, houses and trees"></div>

<footer class="site-footer">
  <div class="f-brand"><span class="brand-dot"></span>Bluefern</div>
  <p class="f-copy">©2022 by Bluefern Safety</p>

  <h4 class="f-head" style="left:424px;top:58px">Contact Us</h4>
  <p class="f-line" style="left:434px;top:100px"><svg width="18" height="18" viewBox="0 0 24 24" fill="none" stroke="#fff" stroke-width="1.8"><path d="M5 3h4l2 5-3 2a12 12 0 006 6l2-3 5 2v4a2 2 0 01-2 2A18 18 0 013 5a2 2 0 012-2z"/></svg>021 5550 4120</p>
  <p class="f-line" style="left:434px;top:134px"><svg width="18" height="16" viewBox="0 0 24 20" fill="none" stroke="#fff" stroke-width="1.8"><rect x="2" y="2" width="20" height="16" rx="1"/><path d="M2 3l10 8 10-8"/></svg>info@bluefernworks.com</p>

  <h4 class="f-head" style="left:714px;top:64px">Quicklinks</h4>
  <a class="f-link" style="top:96px">Home</a>
  <a class="f-link" style="top:120px">About Us</a>
  <a class="f-link" style="top:148px">Products</a>
  <a class="f-link" style="top:174px">Contact Us</a>

  <span class="social" style="left:941px"></span>
  <span class="social" style="left:981px"></span>
  <span class="social" style="left:1020px"></span>
</footer>

</body>
</html>
```